Bref créative
Stationery for bright harbor company
Stationery for my company
Professional
Farhan Tariq Baloch
General Manager
Prince Faisal Street,
Al Warood,
Riyadh,
Saudi Arabia.
P.O.Box:5831-6-40921-3158.
farhan@br1ghth4rb0r.example
www.br1ghth4rb0r.example
C.R.
I want something creative, plus if it is possible can you put the information editable so I can put the other names and titles for the other co - workers
My logo or something creative
logo to be used
like this

```html
<!DOCTYPE html>
<html lang="en">
<head>
<meta charset="utf-8">
<title>Bright Harbor Stationery</title>
<link rel="stylesheet" href="https://fonts.googleapis.com/css2?family=Arimo:wght@400;700&display=swap">
<style>
  :root {
    --page-bg: #5b5e61;
    --card-white: #ffffff;
    --card-shade: #e7e9eb;
    --brand-blue: #1f5f8f;
    --brand-blue-dark: #0f3d63;
    --brand-blue-light: #3f86bd;
    --ink: #3a3f44;
    --ink-soft: #5d646b;
    --mark-grey: #4a4f55;
  }
  * { margin: 0; padding: 0; box-sizing: border-box; }
  html, body { width: 1200px; height: 821px; overflow: hidden; }
  body {
    background: var(--page-bg);
    font-family: "Arimo", Arial, sans-serif;
    position: relative;
  }
  .card {
    position: absolute;
    border-radius: 14px;
    overflow: hidden;
    box-shadow: 0 6px 18px rgba(0,0,0,0.35);
  }
  /* Front card */
  .card-front {
    left: 312px; top: 29px; width: 557px; height: 355px;
    background: linear-gradient(180deg, var(--card-white) 60%, var(--card-shade) 100%);
  }
  .front-band {
    position: absolute; left: 0; top: 38px; width: 100%; height: 106px;
    background: linear-gradient(90deg, #ffffff 0%, #9dbbd4 30%, var(--brand-blue) 55%, var(--brand-blue-dark) 100%);
  }
  .front-brand {
    position: absolute; left: 26px; top: 150px;
    display: flex; align-items: center; gap: 10px;
  }
  .brand-dot {
    width: 34px; height: 34px; border-radius: 50%;
    background: var(--brand-blue);
  }
  .brand-name {
    font-weight: 700; font-size: 22px; letter-spacing: 0.5px;
    color: var(--mark-grey);
  }
  .person {
    position: absolute; left: 269px; top: 60px; color: #fff;
  }
  .person-name { font-weight: 700; font-size: 14px; }
  .person-title { font-size: 12.5px; margin-top: 6px; }
  .contact {
    position: absolute; left: 269px; top: 168px;
    font-size: 12.5px; line-height: 16px; color: var(--ink);
  }
  .contact .gap { height: 16px; }
  .contact .web { margin-top: 16px; color: var(--brand-blue); }
  /* Back cards */
  .card-back {
    top: 475px; width: 490px; height: 317px;
    display: flex; align-items: center; justify-content: center; gap: 14px;
  }
  .card-back-white {
    left: 91px;
    background: linear-gradient(180deg, #ffffff 0%, var(--card-shade) 100%);
  }
  .card-back-blue {
    left: 605px;
    background: linear-gradient(180deg, var(--brand-blue-light) 0%, var(--brand-blue) 45%, var(--brand-blue-dark) 100%);
  }
  .back-dot {
    width: 70px; height: 70px; border-radius: 50%;
  }
  .card-back-white .back-dot { background: var(--mark-grey); }
  .card-back-blue .back-dot { background: #2d6fa2; }
  .back-name { font-weight: 700; font-size: 34px; letter-spacing: 0.5px; }
  .card-back-white .back-name { color: var(--mark-grey); }
  .card-back-blue .back-name { color: #4c88b8; }
</style>
</head>
<body>
  <section class="card card-front">
    <div class="front-band"></div>
    <div class="front-brand">
      <span class="brand-dot"></span>
      <span class="brand-name">BRIGHTHARBOR</span>
    </div>
    <div class="person">
      <div class="person-name">Farhan Tariq Baloch</div>
      <div class="person-title">General Manager</div>
    </div>
    <div class="contact">
      <div>Prince Faisal Street, Al Warood,</div>
      <div>Riyadh, Saudi Arabia.</div>
      <div>P.O.Box:5831-6-40921-3158.</div>
      <div class="gap"></div>
      <div>P: +(966) (01) 4720581</div>
      <div>C: +(966) 551207364</div>
      <div>F: +(966) (01) 4720582</div>
      <div>E: farhan@br1ghth4rb0r.example</div>
      <div class="web">www.br1ghth4rb0r.example</div>
    </div>
  </section>

  <section class="card card-back card-back-white">
    <span class="back-dot"></span>
    <span class="back-name">Brightharbor</span>
  </section>

  <section class="card card-back card-back-blue">
    <span class="back-dot"></span>
    <span class="back-name">Brightharbor</span>
  </section>
</body>
</html>
```